Flier Template in Microsoft Word

We need to a have a flier about farm practices developed in Microsoft Word. Each farm will able to add their own logos and photos. We will give them a model that they can customize.

We want a traditional "country" flavor. Green colors and earth tones are best. Please use the photos we have provided.

The final product must be in Microsoft Word for our farmers to customize.
Updates

All designers: Please have a white background (maybe with a watermark). Our client will print these on white paper using a desktop printer. Thank you!

Target Market(s)

People who shop at Farmer's Markets, join CSAs, and enjoy cooking with fresh vegetables.

Industry/Entity Type

Farm

Font styles to use
Serif

Requirements
Must have
• Must use the text and general layout of the Microsoft Word document attached
Must use the pictures we provided.
Final product must be in Microsoft Word
Must be able to easily swap out the logo at the top
Must be able to print on white paper on a desktop printer
Nice to have
• A nice header that looks like a farm or food on the table
A nice watermark or background to make the flier look polished
Should not have
• Do not change the photos
Do not use high tech fonts or graphic treatments

```html
<!DOCTYPE html>
<html lang="en">
<head>
<meta charset="utf-8">
<title>Sustainable Grazing</title>
<link rel="stylesheet" href="https://fonts.googleapis.com/css2?family=Roboto:wght@400;500;700&display=swap">
<style>
  :root {
    --green-dark: #1b6a26;
    --green-mid: #2f8a34;
    --green-light: #5fae4a;
    --heading: #1e6b2a;
    --text: #222;
    --white: #fff;
    --sky: #b9d4e8;
    --pasture: #7f9a4e;
    --earth: #8a6a45;
  }
  html, body { margin: 0; padding: 0; overflow: hidden; background: var(--white); }
  .flier {
    position: relative;
    width: 927px;
    height: 1200px;
    overflow: hidden;
    background: var(--white);
    font-family: "Roboto", Arial, sans-serif;
    color: var(--text);
  }
  .header-band {
    position: absolute; left: 0; top: 0; width: 927px; height: 139px;
    background: linear-gradient(180deg, var(--green-light) 0%, var(--green-mid) 35%, var(--green-dark) 100%);
  }
  .logo-circle {
    position: absolute; left: 20px; top: 17px; width: 106px; height: 106px;
    border-radius: 50%; background: var(--white);
  }
  .header-title {
    position: absolute; left: 150px; top: 50px; margin: 0;
    font-size: 28px; font-weight: 700; color: var(--white);
  }
  .partner-mark {
    position: absolute; left: 759px; top: 6px; width: 159px; height: 124px;
    background: var(--white); display: flex; align-items: center; justify-content: center;
    gap: 8px; box-sizing: border-box; border: 1px solid #d8d8d8;
  }
  .partner-mark .dot { width: 14px; height: 14px; border-radius: 50%; background: var(--green-light); }
  .partner-mark .name { font-size: 16px; font-weight: 500; color: var(--green-dark); }
  .page-title {
    position: absolute; left: 39px; top: 162px; margin: 0;
    font-size: 29px; font-weight: 700; color: var(--heading);
  }
  .section-heading {
    position: absolute; left: 38px; margin: 0;
    font-size: 25px; font-weight: 700; color: var(--heading);
  }
  .body-copy {
    position: absolute; left: 39px; margin: 0;
    font-size: 16.2px; line-height: 31px; text-align: justify;
  }
  .photo {
    position: absolute;
  }
  .photo-farmer {
    left: 636px; top: 235px; width: 259px; height: 166px;
    background: linear-gradient(180deg, #a8c6d8 0%, #7fa15c 45%, #5f8a3a 100%);
  }
  .photo-creek-herd {
    left: 102px; top: 827px; width: 334px; height: 215px;
    background: linear-gradient(180deg, var(--sky) 0%, #8a9a88 25%, var(--pasture) 50%, var(--earth) 100%);
  }
  .photo-creek-fenced {
    left: 497px; top: 827px; width: 335px; height: 215px;
    background: linear-gradient(180deg, #c9dcec 0%, #8fa07a 28%, #8aa54f 60%, #9a8a3c 100%);
  }
  .meadow-border {
    position: absolute; left: 0; top: 1061px; width: 927px; height: 139px;
    background: linear-gradient(180deg, rgba(255,255,255,0) 0%, #a8d86a 40%, #4f9a2c 100%);
  }
</style>
</head>
<body>
<div class="flier">
  <header>
    <div class="header-band"></div>
    <div class="logo-circle"></div>
    <h2 class="header-title">Text Here</h2>
    <div class="partner-mark"><span class="dot"></span><span class="name">Ridgeline RC&amp;D</span></div>
  </header>

  <h1 class="page-title">Sustainable Grazing</h1>

  <h2 class="section-heading" style="top:229px;">Who We Are</h2>
  <p class="body-copy" style="top:268px; width:567px;">Brookhollow Dairy Farm is a third generation dairy farm located on 64 acres in the Maple Run Valley.&nbsp; We raise holsteins to produce milk and also raise hens for eggs.&nbsp; We sell much of our milk, as well as&nbsp; cheese, yogurt and baked goods directly from the farm.</p>
  <div class="photo photo-farmer" role="img" aria-label="Farmer standing in front of a red tractor in a green field"></div>

  <h2 class="section-heading" style="top:428px;">What Have We Done</h2>
  <p class="body-copy" style="top:459px; width:852px;">At Brookhollow Dairy Farm, we take care of our animals and our animals help us take care of the land.&nbsp; Corn and other grains are not a natural part of a cows’ diet, so we don’t feed them that.&nbsp; Instead, we let them roam the pastures eating grass and other plants.&nbsp; We move the cows from pasture to pasture on a thoughtful schedule to prevent overgrazing, and this reduces soil erosion and water pollution.&nbsp; Our animals are happier and our land and water is healthier.</p>

  <h2 class="section-heading" style="top:631px;">When and Where We Did It</h2>
  <p class="body-copy" style="top:668px; width:852px;">In 2010, we had our cows in a stall barn and corn or soybeans in our fields.&nbsp; We looked into switching some of our acreage from crops to pasture and soon realized that it would beneficial to our cows and our soil.&nbsp; We then installed fencing to divide the fields into smaller paddocks and in spring 2011, we planted a seed mixture containing plants that provide the nutrition our cows need and that provides support for the soil.</p>

  <div class="photo photo-creek-herd" role="img" aria-label="Cattle grazing in a pasture beside a creek with hills behind"></div>
  <div class="photo photo-creek-fenced" role="img" aria-label="Fenced creek buffer running through a green pasture"></div>

  <div class="meadow-border" role="img" aria-label="Grass border with daisies and a ladybug"></div>
</div>
</body>
</html>
```